Potato chips bag design of 85 gram for Greek and East Europe market

I want a new design for a new potato chips bag for the Greek market. The product is going to be all natural ingredient, gluten free, preservatives free, allergen free from Greek organic potatoes . Thick cut, marinated potatoes that are premium vs others. For packaging we want it to stand out on shelf. Have a Matt film . It will be called Korvella Goldleaf. Salt and Oregano flavors to start with.
Ideally to stand out on shelf we were thinking to have a black/white Color pallet and have an artistic pattern printed like the pictures attached. But of course open to ideas.
Target Market(s)
Greece and East Europe
Industry/Entity Type
Snacks Packaged goods
Requirements
Must have
- Matt film that stands out on shelf . 85 grams bag so 25cm tall and 15 cms length
Nice to have
- Ideally black/white pallet as it looks more premium. Patterns artistic that will make it look like art.
Should not have
- Traditional Tovin type of design (red-green colors etc)

```html
<!DOCTYPE html>
<html lang="en">
<head>
<meta charset="UTF-8">
<title>Korvella Goldleaf – Chip Bag Range</title>
<link rel="stylesheet" href="https://fonts.googleapis.com/css2?family=Barlow+Condensed:wght@500;600&family=Anton&display=swap">
<style>
  :root {
    --canvas: #ffffff;
    --bag-black: #1b1b1b;
    --bag-charcoal: #242424;
    --texture-light: #333333;
    --texture-mid: #2a2a2a;
    --oregano: #2f8f3b;
    --oregano-dark: #1f6e2a;
    --salt: #2c8494;
    --salt-dark: #1f6a78;
    --gold: #e9c572;
    --white: #f6f6f6;
    --chip-light: #f7dc8a;
    --chip-deep: #e2b446;
  }
  * { box-sizing: border-box; margin: 0; padding: 0; }
  html, body { width: 1200px; height: 1200px; overflow: hidden; background: var(--canvas); }
  .canvas { position: relative; width: 1200px; height: 1200px; }

  .bag {
    position: absolute; top: 168px; width: 524px; height: 850px;
    background: var(--bag-black); overflow: hidden;
    font-family: "Barlow Condensed", sans-serif;
  }
  .bag--oregano { left: 47px; --accent: var(--oregano); --accent-dark: var(--oregano-dark); }
  .bag--salt { left: 605px; --accent: var(--salt); --accent-dark: var(--salt-dark); background: var(--bag-charcoal); }

  .bag__pattern {
    position: absolute; inset: 0;
    background:
      radial-gradient(ellipse 180px 140px at 18% 30%, var(--texture-light) 0%, transparent 100%),
      radial-gradient(ellipse 200px 160px at 35% 62%, var(--texture-light) 0%, transparent 100%),
      radial-gradient(ellipse 160px 120px at 80% 78%, var(--texture-mid) 0%, transparent 100%),
      radial-gradient(ellipse 220px 140px at 20% 95%, var(--texture-mid) 0%, transparent 100%),
      linear-gradient(175deg, var(--texture-mid) 0%, transparent 60%);
  }
  .bag__herb {
    position: absolute; left: 0; top: 0; width: 300px; height: 145px;
    border-bottom-right-radius: 60% 80%;
  }
  .bag--oregano .bag__herb { background: linear-gradient(160deg, #3fa84a 0%, #237a2c 60%, rgba(27,27,27,0) 100%); }
  .bag--salt .bag__herb { background: linear-gradient(160deg, #f2f2f4 0%, #c9c9cf 55%, rgba(36,36,36,0) 100%); }

  .bag__chips {
    position: absolute; left: 0; top: 0; width: 524px; height: 540px;
    background: radial-gradient(ellipse at 68% 45%, var(--chip-light) 0%, var(--chip-deep) 75%);
    clip-path: polygon(263px 10px, 300px 0, 524px 0, 524px 500px, 470px 535px, 420px 480px, 338px 455px, 300px 430px, 248px 400px, 238px 340px, 228px 270px, 190px 220px, 167px 155px, 200px 90px);
  }

  .flavor-tag {
    position: absolute; left: 43px; top: 340px; width: 163px; height: 68px;
    background: var(--accent); text-align: center; padding-top: 4px;
  }
  .flavor-tag__name { display: block; color: var(--gold); font-weight: 600; font-size: 40px; line-height: 40px; }
  .flavor-tag__sub { display: block; color: var(--white); font-weight: 600; font-size: 15px; letter-spacing: 4px; line-height: 18px; }

  .brand__line1 {
    position: absolute; left: 0; right: 0; top: 542px; text-align: center;
    color: var(--white); font-weight: 600; font-size: 78px; line-height: 70px; letter-spacing: 6px;
  }
  .brand__band {
    position: absolute; left: 47px; top: 612px; width: 440px; height: 146px;
    background: linear-gradient(180deg, var(--accent) 0%, var(--accent-dark) 100%);
  }
  .brand__line2 {
    position: absolute; left: 47px; width: 440px; top: 616px; text-align: center;
    font-family: "Anton", sans-serif; color: var(--white); font-size: 82px; line-height: 96px; letter-spacing: 6px;
  }
  .brand__tagline {
    position: absolute; left: 47px; width: 440px; top: 714px; text-align: center;
    color: var(--white); font-weight: 600; font-size: 25px; letter-spacing: 5px; line-height: 28px;
  }

  .facts { position: absolute; top: 768px; color: var(--gold); font-weight: 600; font-size: 21px; line-height: 22px; }
  .facts--cut { left: 38px; }
  .facts--marinated { left: 176px; }
  .facts--weight { left: 394px; text-align: center; }
  .facts__grams { display: block; font-size: 50px; line-height: 52px; margin-top: 2px; }
</style>
</head>
<body>
<div class="canvas">

  <section class="bag bag--oregano">
    <div class="bag__pattern" role="img" aria-label="Dark line-art leaf pattern"></div>
    <div class="bag__herb" role="img" aria-label="Fresh oregano leaves"></div>
    <div class="bag__chips" role="img" aria-label="Pile of golden thick-cut potato chips"></div>
    <div class="flavor-tag"><span class="flavor-tag__name">OREGANO</span><span class="flavor-tag__sub">FLAVORS</span></div>
    <div class="brand__line1">KORVELLA</div>
    <div class="brand__band"></div>
    <div class="brand__line2">GOLDLEAF</div>
    <div class="brand__tagline">PREMIUM POTATOES CHIPS</div>
    <div class="facts facts--cut">THICK CUT</div>
    <div class="facts facts--marinated">MARINATED POTATOES</div>
    <div class="facts facts--weight">NET WEIGHT<span class="facts__grams">85g</span></div>
  </section>

  <section class="bag bag--salt">
    <div class="bag__pattern" role="img" aria-label="Grey hand-drawn doodle pattern"></div>
    <div class="bag__herb" role="img" aria-label="Coarse sea salt crystals"></div>
    <div class="bag__chips" role="img" aria-label="Pile of golden thick-cut potato chips"></div>
    <div class="flavor-tag"><span class="flavor-tag__name">SALT</span><span class="flavor-tag__sub">FLAVORS</span></div>
    <div class="brand__line1">KORVELLA</div>
    <div class="brand__band"></div>
    <div class="brand__line2">GOLDLEAF</div>
    <div class="brand__tagline">PREMIUM POTATOES CHIPS</div>
    <div class="facts facts--cut">THICK CUT</div>
    <div class="facts facts--marinated">MARINATED POTATOES</div>
    <div class="facts facts--weight">NET WEIGHT<span class="facts__grams">85g</span></div>
  </section>

</div>
</body>
</html>
```